Professional Website

We are looking for a new website for our Staffing Company. Attached is a document with all the details and pages needed along with some examples of others websites.

We want a professional Look and feel around the same color theme as the attached Vivid Vision.

We currently host our site on SiteKarn.io. If the winning designer can also add to SiteKarn, that is a plus.

```html
<!DOCTYPE html>
<html lang="en">
<head>
<meta charset="utf-8">
<title>CrewLine Staffing</title>
<link rel="stylesheet" href="https://fonts.googleapis.com/css2?family=Poppins:wght@400;500;600;700&family=Michroma&display=swap">
<style>
:root{
  --blue:#2a3cc4;
  --blue-dark:#2b2f93;
  --ink:#222;
  --muted:#6d6d6d;
  --green:#1f7a44;
  --dark:#1e1e1e;
  --line:#e5e5e5;
  --white:#fff;
}
*{box-sizing:border-box;margin:0;padding:0}
html,body{width:1200px;height:3948px;overflow:hidden}
body{position:relative;font-family:"Poppins",sans-serif;color:var(--ink);background:var(--white)}
.abs{position:absolute}
.wide{font-family:"Michroma",sans-serif;letter-spacing:.28em;text-transform:uppercase}
.btn{position:absolute;display:flex;align-items:center;justify-content:center;font-weight:600;border-radius:5px}
.btn-blue{background:var(--blue);color:#fff;box-shadow:0 4px 10px rgba(0,0,0,.25)}
/* top bar */
.topbar{top:0;left:0;width:1200px;height:43px;background:#f4f4f4;font-size:15px;color:#333}
.topbar .hotline{left:78px;top:12px;display:flex;gap:8px;align-items:center}
.socials{right:100px;top:13px;display:flex;gap:9px}
.socials span{width:16px;height:16px;border-radius:50%;background:#333}
/* nav */
.nav{top:43px;left:0;width:1200px;height:77px;background:#fff}
.brand{left:70px;top:18px;font-size:30px;font-weight:700;color:var(--green);display:flex;align-items:center;gap:8px}
.brand i{width:14px;height:14px;background:var(--green)}
.menu{left:279px;top:32px;display:flex;gap:28px;font-size:15px;color:#333}
.menu .on{color:var(--blue)}
.logins{right:86px;top:21px;display:flex;gap:8px}
.logins span{background:var(--blue);color:#fff;font-size:14px;height:42px;padding:0 14px;border-radius:5px;display:flex;align-items:center;gap:6px}
/* hero */
.hero{top:120px;left:0;width:1200px;height:600px;background:linear-gradient(90deg,#c9b9a8 0%,#b79b85 25%,#5f7690 55%,#2f4b72 80%,#24395e 100%)}
.hero h1{position:absolute;left:599px;top:150px;white-space:nowrap;font-family:"Michroma",sans-serif;font-weight:400;font-variant:small-caps;font-size:28px;line-height:43px;color:#fff;letter-spacing:.1em}
.hero p{position:absolute;left:599px;top:283px;width:480px;font-size:14px;line-height:28px;color:#fff}
.hero .b1{left:599px;top:388px;width:220px;height:55px;font-size:17px}
.hero .b2{left:829px;top:385px;width:202px;height:58px;font-size:17px;color:#fff;border:1.5px solid #fff;background:transparent}
.dots{left:564px;top:564px;display:flex;gap:4px}
.dots span{width:12px;height:12px;border-radius:50%;background:#fff}
.dots span.o{background:transparent;border:1.5px solid #fff}
.side{right:0;top:353px;width:43px}
.side div{height:46px;background:var(--green);margin-bottom:1px;display:flex;align-items:center;justify-content:center}
/* mission */
.m-back{left:63px;top:791px;width:366px;height:386px;background:#e3e7e6}
.m-frame{left:96px;top:816px;width:176px;height:170px;border:2px solid var(--blue-dark)}
.m-ph1{left:112px;top:829px;width:365px;height:387px;background:linear-gradient(160deg,#d9dde2,#8a8f99 60%,#4a4f5c)}
.m-ph2{left:242px;top:1022px;width:314px;height:270px;background:linear-gradient(150deg,#c4a98d,#8c7565 50%,#3d3f48);box-shadow:0 3px 10px rgba(0,0,0,.25)}
.mission{left:644px;top:826px;width:437px}
.mission h2{font-size:28px;font-weight:400}
.bar{width:81px;height:3px;background:var(--blue-dark);margin:22px 0 28px}
.mission p{font-size:13.5px;line-height:27px;color:var(--muted);text-align:justify}
.mission h3{font-size:20px;font-weight:600;color:var(--blue-dark);margin:22px 0 12px}
.mission .btn{position:relative;width:201px;height:57px;font-size:17px;margin-top:24px}
/* jobs */
.jobs{top:1361px;left:0;width:1200px;height:780px;background:var(--blue-dark)}
.jobs h2{position:absolute;top:82px;width:1200px;text-align:center;color:#fff;font-size:30px;font-weight:400}
.jobs .cbar{position:absolute;left:559px;top:130px;width:81px;height:3px;background:#fff}
.jobs .lead{position:absolute;left:230px;top:155px;width:740px;text-align:center;color:#fff;font-size:15.5px;line-height:28px}
.job{position:absolute;top:241px;width:317px;color:#fff}
.job .img{height:256px}
.job h4{font-size:16px;font-weight:700;margin:12px 0 8px}
.job p{font-size:14px;line-height:27px;padding-left:2px}
.job .ap{position:absolute;top:371px;left:2px;width:124px;height:41px;border:1.5px solid #fff;border-radius:5px;font-size:14px;font-weight:600;display:flex;align-items:center;justify-content:center}
.jobs .arr{position:absolute;top:378px}
.jdots{left:584px;top:697px;display:flex;gap:4px}
.jdots span{width:13px;height:13px;border:1.5px solid #fff;border-radius:2px}
.jdots span.f{background:#fff}
/* contact */
.contact-h{top:2205px;width:1200px;text-align:center;font-size:30px;font-weight:400}
.office-img{top:2298px;width:466px;height:323px}
.office{top:2548px;width:431px;height:254px;background:#fff;box-shadow:0 3px 12px rgba(0,0,0,.18);text-align:center;padding-top:32px}
.office h5{font-family:"Michroma",sans-serif;font-weight:400;font-size:18px;letter-spacing:.2em}
.office .addr{font-family:"Michroma",sans-serif;font-size:16px;letter-spacing:.18em;line-height:33px;margin-top:10px;color:#333}
.office .tel{font-family:"Michroma",sans-serif;font-size:16px;letter-spacing:.18em;margin-top:10px;display:flex;align-items:center;justify-content:center;gap:8px}
.office .apply{font-family:"Michroma",sans-serif;font-size:17px;letter-spacing:.18em;color:var(--blue-dark);text-decoration:underline;margin-top:12px}
.circ{width:60px;height:60px;border-radius:50%;background:#fff;box-shadow:0 2px 8px rgba(0,0,0,.2);display:flex;align-items:center;justify-content:center;top:2430px}
/* about */
.footer-bg{top:3307px;left:0;width:1200px;height:641px;background:linear-gradient(180deg,#242424,#181818)}
.about{left:112px;top:2946px;width:976px;height:454px;background:#fff;box-shadow:0 2px 10px rgba(0,0,0,.15)}
.about h2{position:absolute;left:20px;top:112px;font-size:24px;font-weight:400}
.about p{position:absolute;left:20px;top:178px;width:450px;font-size:12.5px;line-height:28px;color:var(--muted)}
.about .btn{left:17px;top:284px;width:201px;height:57px;font-size:17px}
.about .ph{position:absolute;left:487px;top:19px;width:474px;height:418px;background:linear-gradient(120deg,#6c7a84,#a88a72 55%,#d9c3a9)}
/* footer */
.ask{left:113px;top:3496px;color:#fff;font-size:21px;font-weight:400}
.ask-sub{left:112px;top:3538px;color:#eee;font-size:13.5px}
.field{position:absolute;background:#fff;border-radius:2px;font-size:12px;color:#555;padding:10px 9px}
.submit{left:435px;top:3770px;width:200px;height:56px;font-size:17px;background:var(--blue-dark);color:#fff}
.oc{left:712px;top:3495px;color:#fff;font-size:27px;font-weight:600}
.ci{position:absolute;left:712px;display:flex;gap:14px;color:#fff}
.ci .ico{width:44px;height:44px;border:1.5px solid #fff;border-radius:50%;display:flex;align-items:center;justify-content:center;flex:none}
.ci b{display:block;font-weight:500;font-size:14.5px}
.ci span{font-size:15.5px;line-height:24px}
.rule{left:112px;top:3863px;width:976px;height:1px;background:#555}
.areas{left:112px;top:3894px;color:#fff;font-size:13.5px;display:flex;gap:22px}
.copy{right:112px;top:3893px;color:#fff;font-size:15px}
</style>
</head>
<body>
<div class="abs topbar">
  <div class="abs hotline"><svg width="14" height="14" viewBox="0 0 24 24"><rect width="24" height="24" rx="4" fill="#2b2f93"/><path d="M7 5l3 3-2 2c1 2 3 4 5 5l2-2 3 3-2 2C10 18 6 14 5 7z" fill="#fff"/></svg>Hotline - +1 708-555-0142</div>
  <div class="abs socials"><span></span><span></span><span></span><span></span></div>
</div>
<header class="abs nav">
  <div class="abs brand"><i></i>CrewLine</div>
  <nav class="abs menu"><span class="on">Home</span><span>Jobs</span><span>About</span><span>Contact</span></nav>
  <div class="abs logins"><span>&#9679; Employee Login</span><span>&#9679; Pay Card Login</span><span>&#9679; Partner Bank Login</span></div>
</header>
<section class="abs hero" role="img" aria-label="Smiling professional woman reaching out for a handshake in an office">
  <h1>Recruiting Agency For<br>Temporary And Direct<br>Hire Employees</h1>
  <p>Are you tired of the average temporary staffing agency that sends unqualified warm bodies? We're the first and only recruiting agency specializing in long-term temporary and direct hire staffing.</p>
  <div class="btn btn-blue b1">I'm looking for a Job</div>
  <div class="btn b2">I need Employees</div>
  <div class="abs dots"><span></span><span></span><span class="o"></span><span></span><span></span></div>
</section>
<div class="abs side">
  <div><svg width="16" height="16" viewBox="0 0 24 24"><path d="M6 3l4 4-2 3c1 2 4 5 6 6l3-2 4 4-3 3C10 21 3 14 3 6z" fill="#fff"/></svg></div>
  <div><svg width="16" height="16" viewBox="0 0 24 24"><path d="M4 14a8 8 0 0116 0v4h-4v-5h2a6 6 0 00-12 0h2v5H4z" fill="#fff"/></svg></div>
  <div><svg width="16" height="14" viewBox="0 0 24 18"><rect width="24" height="18" rx="2" fill="#fff"/><path d="M1 2l11 8 11-8" stroke="#1f7a44" stroke-width="2" fill="none"/></svg></div>
</div>

<div class="abs m-back"></div>
<div class="abs m-frame"></div>
<div class="abs m-ph1" role="img" aria-label="Colleagues talking across a desk in a bright office"></div>
<div class="abs m-ph2" role="img" aria-label="Team meeting around a table with laptops and notes"></div>
<div class="abs mission">
  <h2 class="wide">Our Mission</h2>
  <div class="bar"></div>
  <p>We help people with our best services, Not only at work, but in life.CrewLine Team focuses its efforts on the Company's most valuable assets-its people. That is accomplished through the recruitment, hiring &amp; retention of a diverse workforce.</p>
  <h3>Why Partner up with us?</h3>
  <p>CrewLine Team always does the best to have relationships that go deep into the market. We won't rely simply on hope and prayers, we interview 1000's and as many more candidates and have a remarkable way of getting to know them,</p>
  <div class="btn btn-blue">Read More</div>
</div>

<section class="abs jobs">
  <h2 class="wide">Jobs Panel</h2>
  <div class="cbar"></div>
  <p class="lead">Are you tired of jumping from one temporary staffing agency to the next? At CrewLine, we provide great pay, PTO/Vacation pay, and much more.</p>
  <svg class="arr" style="left:78px" width="16" height="24" viewBox="0 0 16 24"><path d="M12 3L4 12l8 9" stroke="#fff" stroke-width="2.5" fill="none"/></svg>
  <svg class="arr" style="left:1102px" width="16" height="24" viewBox="0 0 16 24"><path d="M4 3l8 9-8 9" stroke="#fff" stroke-width="2.5" fill="none"/></svg>
  <div class="job" style="left:112px"><div class="img" role="img" aria-label="Welder working with sparks flying" style="background:linear-gradient(135deg,#3b3f46,#8d98a8 50%,#2a2d33)"></div><h4>Welders</h4><p>We are hiring for, a reputed metal display company located in Hammond, IN...</p><div class="ap">Apply Now</div></div>
  <div class="job" style="left:443px"><div class="img" role="img" aria-label="Log loader machine at sunset" style="background:linear-gradient(135deg,#8aa3b8,#e9d9a8 45%,#5a6a3a)"></div><h4>Material Handlers</h4><p>You will be expected to work with a team and efficiently coordinate with them...</p><div class="ap">Apply Now</div></div>
  <div class="job" style="left:773px"><div class="img" role="img" aria-label="Smiling worker in a knit hat leaning on lumber" style="background:linear-gradient(135deg,#d8dde2,#8a8276 55%,#c9b08a)"></div><h4>General Labour</h4><p>Hiring general labor is our focus and we help the right persons get employed...</p><div class="ap">Apply Now</div></div>
  <div class="abs jdots"><span class="f"></span><span></span></div>
</section>

<h2 class="abs contact-h wide">Contact Us</h2>
<div class="abs circ" style="left:27px"><svg width="12" height="18" viewBox="0 0 12 18"><path d="M9 2L3 9l6 7" stroke="#222" stroke-width="2" fill="none"/></svg></div>
<div class="abs circ" style="left:1101px"><svg width="12" height="18" viewBox="0 0 12 18"><path d="M3 2l6 7-6 7" stroke="#222" stroke-width="2" fill="none"/></svg></div>
<div class="abs office-img" style="left:123px;background:linear-gradient(180deg,#e6ebef,#8d96a0 55%,#4a5560)" role="img" aria-label="Chicago riverfront skyline"></div>
<div class="abs office-img" style="left:612px;background:linear-gradient(180deg,#8fb0cf,#b7c6d4 45%,#4e5a66)" role="img" aria-label="City skyline with a tall tower at dusk"></div>
<div class="abs office" style="left:141px"><h5>Chicago, IL</h5><div class="addr">4120 W. Harbor Ave. Chicago,<br>IL 60601</div><div class="tel"><svg width="14" height="14" viewBox="0 0 24 24"><path d="M6 3l4 4-2 3c1 2 4 5 6 6l3-2 4 4-3 3C10 21 3 14 3 6z" fill="#2b2f93"/></svg>312-555-0187</div><div class="apply">APPLY ONLINE</div></div>
<div class="abs office" style="left:629px"><h5>Hammond, IN</h5><div class="addr">1835 Calumet Rd.<br>Hammond, IN 46320</div><div class="tel"><svg width="14" height="14" viewBox="0 0 24 24"><path d="M6 3l4 4-2 3c1 2 4 5 6 6l3-2 4 4-3 3C10 21 3 14 3 6z" fill="#2b2f93"/></svg>219-555-0163</div><div class="apply">APPLY ONLINE</div></div>

<div class="abs footer-bg"></div>
<div class="abs about">
  <h2 class="wide">About CrewLine</h2>
  <p>Are you tired of the average temporary staffing agency that sends unqualified warm bodies? We're the first and only recruiting agency specializing in long-term temporary and direct hire staffing</p>
  <div class="btn btn-blue">Read More</div>
  <div class="ph" role="img" aria-label="Smiling businesswoman shaking hands with a colleague"></div>
</div>

<h3 class="abs ask wide">Got a question?</h3>
<p class="abs ask-sub">We're here to help. Send us an email or call us at 312-555-0187</p>
<div class="field" style="left:112px;top:3578px;width:256px;height:43px">Name</div>
<div class="field" style="left:379px;top:3578px;width:256px;height:43px">Email</div>
<div class="field" style="left:112px;top:3632px;width:521px;height:43px">Phone Number</div>
<div class="field" style="left:112px;top:3685px;width:521px;height:66px">Message</div>
<div class="btn submit">Submit Now</div>

<h3 class="abs oc">OUR CONTACTS</h3>
<div class="ci" style="top:3547px"><div class="ico"><svg width="14" height="18" viewBox="0 0 14 20"><path d="M7 0a7 7 0 017 7c0 5-7 13-7 13S0 12 0 7a7 7 0 017-7z" fill="#fff"/><circle cx="7" cy="7" r="2.5" fill="#1e1e1e"/></svg></div><div><b>ADDRESS</b><span>4120 W. Harbor Ave. Chicago,<br>IL 60601</span></div></div>
<div class="ci" style="top:3634px"><div class="ico"><svg width="16" height="16" viewBox="0 0 24 24"><path d="M6 3l4 4-2 3c1 2 4 5 6 6l3-2 4 4-3 3C10 21 3 14 3 6z" fill="#fff"/></svg></div><div><b>PHONE</b><span>+1 312-555-0187</span></div></div>
<div class="ci" style="top:3702px"><div class="ico"><svg width="16" height="12" viewBox="0 0 24 18"><rect width="24" height="18" rx="2" fill="#fff"/><path d="M1 2l11 8 11-8" stroke="#1e1e1e" stroke-width="2" fill="none"/></svg></div><div><b>EMAIL</b><span>hello@crewlinestaff.com</span></div></div>
<div class="ci" style="top:3776px"><div class="ico"><svg width="18" height="18" viewBox="0 0 24 24"><circle cx="12" cy="12" r="10" fill="#fff"/><path d="M2 12h20M12 2c3 3 3 17 0 20M12 2c-3 3-3 17 0 20" stroke="#1e1e1e" stroke-width="1.5" fill="none"/></svg></div><div><b>WEBSITE</b><span style="font-size:14px">www.crewlinestaff.com</span></div></div>

<div class="abs rule"></div>
<div class="abs areas"><span><b style="font-weight:600">Areas we service</b> - Blue Island</span><span>Alsip</span><span>Romeoville</span></div>
<div class="abs copy">© 2022 All Rights Reserved</div>
</body>
</html>
```